ALL TEXT Social Media Graphics

We are looking for a series of social media graphics for Instagram (new size: 4:5 (1080 x 1350 pixels) ratio that are ALL TEXT. We want the following quotes below on each graphic; one quote per graphic. AND, In very small letters at the bottom of each graphic, add @PaulaWrenLive
The look and feel of these graphics should be complimentary to the color palette attached below; but keep them simple. But the design is up to you; at the end of this document, I provided various samples of all text graphics that I like as examples.
The Quotes are in the attached WORD document
women trying to lose weight

```html
<!DOCTYPE html>
<html lang="en">
<head>
<meta charset="utf-8">
<title>Summer Glow Reset – Text Graphics</title>
<link href="https://fonts.googleapis.com/css2?family=Bebas+Neue&family=Oswald:wght@500;600;700&family=Jost:wght@500&family=Caveat+Brush&display=swap" rel="stylesheet">
<style>
  :root {
    --berry: #ad1c5a;
    --rose: #e6609a;
    --ink: #2a2a2a;
    --blush: #f2c3d6;
    --paper: #ffffff;
  }
  * { margin: 0; padding: 0; box-sizing: border-box; }
  html, body { width: 1200px; height: 1094px; overflow: hidden; background: var(--paper); }
  .canvas { position: relative; width: 1200px; height: 1094px; }

  .post {
    position: absolute;
    width: 262px; height: 326px;
    background: radial-gradient(ellipse at center, #fff 45%, #fbe6ef 72%, var(--blush) 100%);
    text-align: center;
    overflow: hidden;
  }
  .post::before {
    content: ""; position: absolute; left: 0; right: 0; top: 14px;
    height: 3px; background: var(--rose);
  }
  .post__footer {
    position: absolute; left: 0; right: 0; bottom: 9px;
    display: flex; align-items: center; gap: 8px;
  }
  .post__footer::before, .post__footer::after {
    content: ""; flex: 1; height: 3px; background: var(--rose);
  }
  .handle {
    font-family: "Oswald", sans-serif; font-weight: 600;
    font-size: 10px; color: var(--berry); letter-spacing: 0.2px;
  }
  .post__body {
    position: absolute; left: 10px; right: 10px; top: 22px; bottom: 30px;
    display: flex; flex-direction: column; justify-content: center; align-items: center;
  }
  .lead { font-family: "Bebas Neue", sans-serif; color: var(--ink); font-size: 21px; line-height: 0.98; }
  .lead--sm { font-size: 18px; }
  .headline { font-family: "Oswald", sans-serif; font-weight: 600; color: var(--berry); font-size: 27px; line-height: 1.15; letter-spacing: -0.3px; text-transform: uppercase; }
  .headline--xl { font-size: 35px; }
  .headline--dark { color: var(--ink); }
  .note { font-family: "Jost", sans-serif; font-weight: 500; color: var(--rose); font-size: 15.5px; line-height: 1.05; }
  .note--sm { font-size: 12.5px; }
  .script { font-family: "Caveat Brush", cursive; color: var(--rose); font-size: 26px; line-height: 1.1; }
  .script--ink { color: var(--ink); }
  .prompt { font-family: "Bebas Neue", sans-serif; color: var(--ink); font-size: 25px; line-height: 1; margin-top: 6px; }
  .keyword { font-family: "Oswald", sans-serif; font-weight: 700; color: var(--berry); font-size: 50px; line-height: 1.1; letter-spacing: -0.5px; text-transform: uppercase; white-space: nowrap; }
</style>
</head>
<body>
<main class="canvas">

  <article class="post" style="left:31px;top:22px">
    <div class="post__body">
      <p class="lead">If your goal is a<br>tiny waist, flat belly, &amp;</p>
      <p class="headline">Drop 30 Pounds</p>
      <p class="note">—this is the plan.</p>
      <p class="prompt" style="margin-top:12px">Comment</p>
      <p class="keyword">“Summer”</p>
      <p class="note">to join the<br>Summer Glow Reset!</p>
    </div>
    <footer class="post__footer"><span class="handle">@PAULAWRENLIVE</span></footer>
  </article>

  <article class="post" style="left:327px;top:22px">
    <div class="post__body">
      <p class="lead lead--sm">You’ve got 8 weeks &amp;<br>the perfect plan to</p>
      <p class="headline headline--xl">Drop 30 Pounds.</p>
      <p class="script script--ink">Let’s Get Snatched</p>
      <p class="note">this summer<br>with the<br>Summer Glow Reset.</p>
      <p class="prompt">Comment</p>
      <p class="keyword">“Summer”!</p>
    </div>
    <footer class="post__footer"><span class="handle">@PAULAWRENLIVE</span></footer>
  </article>

  <article class="post" style="left:624px;top:22px">
    <div class="post__body">
      <p class="script">Don’t Wait</p>
      <p class="lead lead--sm">‘til next summer to get right.</p>
      <p class="script">The Time is NOW.</p>
      <p class="headline">Drop 30 Pounds</p>
      <p class="note">with the<br>Summer Glow Reset.</p>
      <p class="prompt">Comment</p>
      <p class="keyword">“Summer”!</p>
    </div>
    <footer class="post__footer"><span class="handle">@PAULAWRENLIVE</span></footer>
  </article>

  <article class="post" style="left:909px;top:22px">
    <div class="post__body">
      <p class="lead lead--sm">Sis, we’re dropping belly flat &amp;<br>saying goodbye<br>to stubborn pounds.</p>
      <p class="script" style="font-size:30px;margin-top:6px">Join The</p>
      <p class="note">Summer Glow Reset—</p>
      <p class="prompt" style="margin-top:14px">Comment</p>
      <p class="keyword">“Summer”</p>
    </div>
    <footer class="post__footer"><span class="handle">@PAULAWRENLIVE</span></footer>
  </article>

  <article class="post" style="left:31px;top:377px">
    <div class="post__body">
      <p class="lead lead--sm">This summer ain’t over—<br>&amp; neither are your body goals.</p>
      <p class="headline">Drop 30 Pounds</p>
      <p class="script script--ink">With The</p>
      <p class="note">Summer Glow Reset.</p>
      <p class="prompt" style="margin-top:10px">Comment</p>
      <p class="keyword">“Glow Up”</p>
      <p class="note" style="margin-top:6px">to get the plan</p>
    </div>
    <footer class="post__footer"><span class="handle">@PAULAWRENLIVE</span></footer>
  </article>

  <article class="post" style="left:327px;top:377px">
    <div class="post__body">
      <p class="lead">There’s still time</p>
      <p class="headline" style="margin-top:10px">Drop the 30 Pounds</p>
      <p class="note" style="margin-top:6px">and slay this summer.<br>has the blueprint.</p>
      <p class="prompt" style="margin-top:14px">Comment</p>
      <p class="keyword">“Glow Up”</p>
    </div>
    <footer class="post__footer"><span class="handle">@PAULAWRENLIVE</span></footer>
  </article>

  <article class="post" style="left:624px;top:377px">
    <div class="post__body">
      <p class="lead lead--sm">Snatched waist, flat tummy,</p>
      <p class="headline headline--xl headline--dark">30 Pounds</p>
      <p class="script script--ink" style="font-size:30px">Lighter</p>
      <p class="note note--sm">—that’s what the Summer Glow<br>Reset Challenge delivers.</p>
      <p class="prompt" style="margin-top:8px">Comment</p>
      <p class="keyword">“Glow Up”</p>
      <p class="note">to get the plan</p>
    </div>
    <footer class="post__footer"><span class="handle">@PAULAWRENLIVE</span></footer>
  </article>

  <article class="post" style="left:909px;top:377px">
    <div class="post__body">
      <p class="lead lead--sm">Nothing feels better than seeing<br>that scale drop week after week.</p>
      <p class="script">Let’s lose up to</p>
      <p class="headline headline--xl">30 Pounds</p>
      <p class="lead">This summer —together.</p>
      <p class="prompt" style="margin-top:2px">Comment</p>
      <p class="keyword">“Summer”</p>
      <p class="note">to join the<br>Summer Glow Reset!</p>
    </div>
    <footer class="post__footer"><span class="handle">@PAULAWRENLIVE</span></footer>
  </article>

  <article class="post" style="left:31px;top:747px">
    <div class="post__body">
      <p class="lead">You can absolutely be</p>
      <p class="headline">Down 20–30 Pounds</p>
      <p class="script script--ink">By end of Summer.</p>
      <p class="note">All it takes is the right plan<br>—and you’ve found it.</p>
      <p class="prompt" style="margin-top:10px">Comment</p>
      <p class="keyword">“Glow Up”</p>
      <p class="note" style="margin-top:4px">for the Summer<br>Glow Reset!</p>
    </div>
    <footer class="post__footer"><span class="handle">@PAULAWRENLIVE</span></footer>
  </article>

  <article class="post" style="left:327px;top:747px">
    <div class="post__body">
      <p class="lead">You don’t need another diet<br>you need a system that works.</p>
      <p class="headline">Drop 30 Pounds</p>
      <p class="script script--ink">With The</p>
      <p class="note">Summer Glow Reset.</p>
      <p class="prompt" style="margin-top:12px">Comment</p>
      <p class="keyword">“Summer”</p>
      <p class="note" style="margin-top:6px">to start now.</p>
    </div>
    <footer class="post__footer"><span class="handle">@PAULAWRENLIVE</span></footer>
  </article>

</main>
</body>
</html>
```